Invitation

Please design an invitation for March 31st drop in between 10-1 reception to celebrate the opening of Whitfield's Landing and the Residences at 9 N. Birch. 9 N. Birch Street Quarryville, PA 17504. Tour the buildings newly renovated units and commercial space and enjoy refreshments at the reception.

```html
<!DOCTYPE html>
<html lang="en">
<head>
<meta charset="utf-8">
<title>Whitfield's Landing Opening Invitation</title>
<link rel="stylesheet" href="https://fonts.googleapis.com/css2?family=Oswald:wght@400;500;600&family=Open+Sans:wght@400&display=swap">
<style>
  :root {
    --teal: #1d6e72;
    --teal-dark: #1b5d63;
    --ink: #24555d;
    --paper: #ffffff;
    --stage: #e9e9e7;
    --sky-top: #8fa6bf;
    --sky-low: #c9d3dc;
    --facade: #6f7368;
    --street: #3d3d40;
  }
  * { box-sizing: border-box; margin: 0; padding: 0; }
  html, body { width: 1114px; height: 1200px; overflow: hidden; }
  body { background: var(--stage); position: relative; font-family: "Oswald", sans-serif; }

  .card {
    position: absolute; left: 157px; width: 800px; height: 496px;
    background: var(--paper); box-shadow: 0 3px 10px rgba(0,0,0,.22);
  }
  .card--invite { top: 58px; }
  .card--gallery { top: 622px; }

  .card-header { position: absolute; left: 0; top: 0; width: 100%; height: 101px; }
  .venue-address, .event-date {
    position: absolute; top: 42px; font-size: 14px; line-height: 18px;
    color: var(--ink); font-weight: 400; letter-spacing: -0.2px;
  }
  .venue-address { left: 34px; }
  .event-date { right: 16px; text-align: right; }

  .brand {
    position: absolute; left: 50%; top: 32px; transform: translateX(-50%);
    display: flex; align-items: center; gap: 8px; white-space: nowrap;
  }
  .brand-mark { width: 14px; height: 14px; background: var(--teal-dark); }
  .brand-name { font-size: 22px; font-weight: 500; color: var(--teal-dark); letter-spacing: .5px; }

  .photo {
    position: absolute;
    background: linear-gradient(180deg, var(--sky-top) 0%, var(--sky-low) 35%, var(--facade) 55%, #7a7c74 78%, var(--street) 100%);
  }
  .photo--hero { left: 0; top: 101px; width: 800px; height: 347px; }
  .photo--corner { left: 0; top: 101px; width: 396px; height: 343px; }
  .photo--side { left: 402px; top: 101px; width: 398px; height: 168px; }
  .photo--porch { left: 402px; top: 275px; width: 398px; height: 169px; }

  .invite-copy {
    position: absolute; left: 0; top: 101px; width: 800px; height: 347px;
    text-align: center; color: #fff; text-shadow: 0 1px 3px rgba(0,0,0,.45);
  }
  .invite-title { position: absolute; top: 110px; width: 100%; font-size: 33px; font-weight: 500; letter-spacing: -0.5px; }
  .invite-lead { position: absolute; top: 168px; width: 100%; font-size: 16px; line-height: 21px; font-weight: 400; letter-spacing: -0.3px; }
  .invite-note { position: absolute; top: 231px; width: 100%; font-family: "Open Sans", sans-serif; font-size: 10px; letter-spacing: -0.2px; }

  .card-footer { position: absolute; left: 0; bottom: 0; width: 100%; height: 48px; }
  .contact { position: absolute; top: 20px; font-family: "Open Sans", sans-serif; font-size: 10px; color: #222; }
  .contact--email { left: 34px; }
  .contact--web { right: 14px; }
  .phone-band {
    position: absolute; left: 236px; top: 10px; width: 310px; height: 38px;
    background: var(--teal);
    clip-path: polygon(18px 0, 100% 0, calc(100% - 18px) 100%, 0 100%);
    display: flex; align-items: center; justify-content: center; gap: 14px;
  }
  .phone-icon { width: 20px; height: 24px; }
  .phone-number { color: #fff; font-size: 27px; font-weight: 500; letter-spacing: 2.5px; }
  .footer-rule { position: absolute; left: 0; bottom: 0; width: 100%; height: 3px; background: var(--teal); }
</style>
</head>
<body>

<section class="card card--invite">
  <header class="card-header">
    <p class="venue-address">9 N. Birch Street<br>Quarryville, PA 17504</p>
    <div class="brand"><span class="brand-mark"></span><span class="brand-name">Hawthorn Row Properties</span></div>
    <p class="event-date">March 31st<br>drop in between 10-1 reception</p>
  </header>
  <div class="photo photo--hero" role="img" aria-label="Rendering of the renovated corner building with porches under a cloudy sky"></div>
  <div class="invite-copy">
    <h1 class="invite-title">YOU’RE INVITED!</h1>
    <p class="invite-lead">Celebrate the opening of Whitfield's Landing and the Residences at<br>9 N. Birch Street Quarryville, PA 17504</p>
    <p class="invite-note">Tour the buildings newly renovated units and commercial space and enjoy refreshments at the reception.</p>
  </div>
  <footer class="card-footer">
    <span class="contact contact--email">info@hawthornrowproperties.com</span>
    <div class="phone-band">
      <svg class="phone-icon" viewBox="0 0 20 24" aria-hidden="true">
        <rect x="3" y="1" width="14" height="22" rx="2.5" fill="none" stroke="#fff" stroke-width="2"/>
        <line x1="8" y1="19" x2="12" y2="19" stroke="#fff" stroke-width="2"/>
      </svg>
      <span class="phone-number">(717) 555-0148</span>
    </div>
    <span class="contact contact--web">hawthornrow.residentportal.com</span>
    <div class="footer-rule"></div>
  </footer>
</section>

<section class="card card--gallery">
  <header class="card-header">
    <p class="venue-address">9 N. Birch Street<br>Quarryville, PA 17504</p>
    <div class="brand"><span class="brand-mark"></span><span class="brand-name">Hawthorn Row Properties</span></div>
    <p class="event-date">March 31st<br>drop in between 10-1 reception</p>
  </header>
  <div class="photo photo--corner" role="img" aria-label="Rendering of the building corner with storefront and steps"></div>
  <div class="photo photo--side" role="img" aria-label="Rendering of the long side elevation with residence entrance"></div>
  <div class="photo photo--porch" role="img" aria-label="Rendering of the wraparound porch and bay windows"></div>
  <footer class="card-footer">
    <span class="contact contact--email">info@hawthornrowproperties.com</span>
    <div class="phone-band">
      <svg class="phone-icon" viewBox="0 0 20 24" aria-hidden="true">
        <rect x="3" y="1" width="14" height="22" rx="2.5" fill="none" stroke="#fff" stroke-width="2"/>
        <line x1="8" y1="19" x2="12" y2="19" stroke="#fff" stroke-width="2"/>
      </svg>
      <span class="phone-number">(717) 555-0148</span>
    </div>
    <span class="contact contact--web">hawthornrow.residentportal.com</span>
    <div class="footer-rule"></div>
  </footer>
</section>

</body>
</html>
```